"Thank You" card for professional property management agency.

We need to create a DL size "Thank You" card primarily used to thank new clients for their business and referrals.
We are a real estate agency based on Sydney's Northern Beaches. We want the card to feel happy and professional, incorporating our logo.
See our website for details about our business - www.harbourleafrealty.com.au
We have attached our logo in black text and white text as well as some images we have used across our website.
One side must have the ability to hand write a message of thank you on.
I would like this to be a clean and simple design, feel free to use any image supplied, but we are also happy with plain or patterned designs too.

Target Market(s)

Property investors male and female aged 30-60

Industry/Entity Type

Real Estate

Font styles to use
Other font styles liked:
• Please let the designer choose font

Colors

Designer to choose colors to be used in the design.

Requirements
Must have
• DL Size: Full Bleed 213x102mm. Doc size 210x99mm (horizontal)
• Harbour Leaf Realty Logo
• Contact Details:
• info@harbourleafrealty.com.au
• Tel: 0498 217 603
• Level 2, 17 Wattlecombe Rd, Wattlecombe NSW 2187
• "Thank You" somewhere on the card
• Area or side to write message on.
• Design to be provided in editable photoshop PSD file and print ready PDF file
Nice to have
• Sleek professional design that feels "happy or grateful" as it is a thank you card
• Happy to use a plain colour or pattern on one side - it does not have to be an image provided, but feel free to design with either.
Should not have
• should not be too busy, keep it clean and simple.

```html
<!DOCTYPE html>
<html lang="en">
<head>
<meta charset="utf-8">
<title>Harbour Leaf Realty – Thank You Card</title>
<link rel="stylesheet" href="https://fonts.googleapis.com/css2?family=Pinyon+Script&family=Roboto+Condensed:wght@400;700&display=swap">
<style>
  :root {
    --backdrop: #e9e7e4;
    --card: #ffffff;
    --teal: #2b9ea4;
    --teal-deep: #1f8a90;
    --ink: #111111;
    --footer: #2a2a2a;
    --footer-text: #e6e6e6;
    --sky: #17a3dc;
    --sky-soft: #6cc6ea;
    --facade: #cfcac2;
    --garden: #3f6b3a;
    --garden-deep: #24412a;
  }
  * { margin: 0; padding: 0; box-sizing: border-box; }
  html, body {
    width: 1200px;
    height: 701px;
    overflow: hidden;
    background: var(--backdrop);
  }
  .card {
    position: absolute;
    left: 40px;
    top: 82px;
    width: 1120px;
    height: 536px;
    background: var(--card);
    overflow: hidden;
  }
  .card-art {
    position: absolute;
    left: 0;
    top: 0;
    width: 1120px;
    height: 482px;
    display: block;
  }
  .brand-name {
    position: absolute;
    right: 26px;
    top: 62px;
    display: flex;
    align-items: center;
    gap: 10px;
    font-family: "Roboto Condensed", sans-serif;
    font-weight: 700;
    font-size: 27px;
    letter-spacing: 0.2px;
    color: var(--ink);
    text-transform: uppercase;
  }
  .brand-mark {
    width: 12px;
    height: 12px;
    background: var(--teal);
  }
  .thank-you {
    position: absolute;
    right: 36px;
    top: 138px;
    font-family: "Pinyon Script", cursive;
    font-size: 84px;
    line-height: 1.2;
    color: var(--teal);
    white-space: nowrap;
  }
  .contact-bar {
    position: absolute;
    left: 0;
    bottom: 0;
    width: 100%;
    height: 54px;
    background: var(--footer);
    display: flex;
    align-items: center;
    justify-content: center;
    gap: 9px;
    font-family: "Roboto Condensed", sans-serif;
    font-weight: 400;
    font-size: 13px;
    letter-spacing: 0.6px;
    color: var(--footer-text);
    text-transform: uppercase;
    white-space: nowrap;
  }
  .contact-divider { opacity: 0.8; }
</style>
</head>
<body>
  <main class="card">
    <svg class="card-art" viewBox="0 0 1320 568" preserveAspectRatio="none" aria-hidden="false">
      <defs>
        <linearGradient id="photoTones" x1="0" y1="0" x2="0" y2="1">
          <stop offset="0" stop-color="var(--sky)"/>
          <stop offset="0.28" stop-color="var(--sky-soft)"/>
          <stop offset="0.42" stop-color="var(--facade)"/>
          <stop offset="0.68" stop-color="var(--garden)"/>
          <stop offset="1" stop-color="var(--garden-deep)"/>
        </linearGradient>
      </defs>
      <path class="hero-photo" role="img" aria-label="Photo of a modern two-storey home with balconies, landscaped garden and stone stairs under a blue sky"
            d="M0,0 L190,0 C410,12 505,110 530,260 C555,425 620,540 780,560 L780,568 L0,568 Z"
            fill="url(#photoTones)"/>
      <path class="swoosh-thin" d="M200,0 C430,14 520,110 545,260 C570,425 640,545 815,560"
            fill="none" stroke="var(--teal)" stroke-width="3"/>
      <path class="swoosh-band" d="M300,3 C470,40 540,140 560,270 C582,430 660,548 830,562"
            fill="none" stroke="var(--teal)" stroke-width="9"/>
    </svg>

    <div class="brand-name"><span class="brand-mark"></span>Harbour Leaf Realty</div>

    <h1 class="thank-you">Thank You</h1>

    <footer class="contact-bar">
      <span class="contact-address">Level 2, 17 Wattlecombe Rd, Wattlecombe NSW 2187</span>
      <span class="contact-divider">|</span>
      <span class="contact-phone">0498 217 603</span>
      <span class="contact-divider">|</span>
      <span class="contact-email">info@harbourleafrealty.com.au</span>
      <span class="contact-divider">|</span>
      <span class="contact-web">www.harbourleafrealty.com.au</span>
    </footer>
  </main>
</body>
</html>
```